B2B Consulting firm needs a re-fresh of its process diagrams

We are a commercial real estate consulting firm. Think: I wonder who Kovarelli uses when they have to build a new plant and sell the old one? That's us! We have created diagrams that we use to demonstrate to our clients the process of the project that they are about to go through. That is our "frontstage" diagram. We also have a "backstage" diagram that we use to train employees and to ensure that we do not make a stupid mistake! Here is a video showing you a little about what we are wanting https://view.clipframely.com/v/QpRtWz7YbLm2KdFs8JxV

Target Market(s)

B2B - C-suite and business leaders

Industry/Entity Type

Commercial Real Estate

Font styles to use
Sans Serif

Colors
0094D4
00A9DD
6FCCEA
C7EBF8
E9F6FB
EB3D1F
EC4F4E
F09395
F8D3D4
FCEDEE

Requirements
Must have
• Think of it as a infographic - clean and modern
Nice to have
• I would suggest that you look at the infographics that are used by Talmont Trade Quarterly, Prewitt, RDVF and other professional services firms/publications.

```html
<!DOCTYPE html>
<html lang="en">
<head>
<meta charset="utf-8">
<title>Space Acquisition: Purchase &amp; Process Deliverables</title>
<link href="https://fonts.googleapis.com/css2?family=Montserrat:wght@400;500;600&display=swap" rel="stylesheet">
<style>
:root{
  --page:#e4e5e7;
  --card:#ffffff;
  --ink:#2a2f3e;
  --ink-soft:#3a3d45;
  --roles:#2470b8;
  --process:#3a9ad6;
  --deliver:#00aebd;
  --green:#82c043;
  --tint:#f6f6f6;
  --tint-dark:#e3e3e3;
}
*{box-sizing:border-box;margin:0;padding:0}
html,body{width:1200px;height:1200px;overflow:hidden;background:var(--page);font-family:"Montserrat",sans-serif;color:var(--ink-soft)}
.sheet{position:absolute;left:120px;width:960px;height:539px;background:var(--card)}
.sheet--one{top:43px}
.sheet--two{top:617px}
.abs{position:absolute}
.figure-label{left:0;right:0;top:32px;text-align:center;font-size:11.5px;letter-spacing:.3px;color:var(--ink)}
.title{left:0;right:0;top:48px;text-align:center;font-size:29px;font-weight:500;color:var(--ink);letter-spacing:-.2px}
.title span{color:var(--roles)}
.col-head{top:95px;width:289px;height:31px;border-radius:3px;color:#fff;font-size:14.5px;padding-left:17px;line-height:31px}
.col-roles{left:38px}.col-process{left:335px}.col-deliver{left:633px}
.head-roles{background:var(--roles)}.head-process{background:var(--process)}.head-deliver{background:var(--deliver)}
.panel{background:var(--tint)}
.panel--dark{background:var(--tint-dark)}
.group-title{font-size:12.4px;color:var(--roles);font-weight:500}
.people-title{font-size:9.4px;color:var(--roles);font-weight:500;line-height:10.8px}
ul{list-style:none}
.small li{position:relative;font-size:9.2px;line-height:10.2px;padding-left:14px;margin-bottom:1.6px}
.small li::before{content:"";position:absolute;left:0;top:3.5px;width:3px;height:3px;background:var(--roles)}
.tiny li{font-size:8.2px;line-height:8.6px;margin-bottom:2px}
.tiny li::before{top:3px}
.stage{font-size:15px;color:var(--process);font-weight:500}
.stage--teal{color:var(--deliver)}
.step{width:289px;color:#fff;display:flex;align-items:center}
.step--blue{background:var(--process)}
.step--teal{background:var(--deliver)}
.step .num{width:50px;padding-left:16px;font-size:19px;flex:none}
.step .label{flex:1;font-size:12px;line-height:13px;letter-spacing:.2px}
.step svg{flex:none;margin-right:16px}
.step-list li{position:relative;font-size:14.5px;line-height:15px;padding-left:13px;margin:11px 0}
.step-list li::before{content:"";position:absolute;left:0;top:6px;width:4px;height:4px;background:#fff}
.end{width:289px;text-align:center;font-size:11px;letter-spacing:3px;color:var(--ink)}
.deliv li{position:relative;font-size:12.2px;line-height:13px;padding-left:17px;color:var(--ink-soft)}
.deliv li::before{content:"";position:absolute;left:0;top:4.5px;width:3.5px;height:3.5px;background:var(--deliver)}
.deliv .sub li{padding-left:18px;margin:3.8px 0 3.8px 36px}
.deliv--tight li{font-size:11px;line-height:14px}
.deliv--tight li::before{top:5px}
.note-green{background:var(--green);color:#fff;font-size:12px;line-height:15px;padding:0 17px;display:flex;align-items:center}
</style>
</head>
<body>

<section class="sheet sheet--one">
  <p class="abs figure-label">FIGURE 5</p>
  <h1 class="abs title"><span>Space Acquisition:</span> Purchase &amp; Process Deliverables</h1>
  <div class="abs col-head col-roles head-roles">Roles &amp; Responsibilities</div>
  <div class="abs col-head col-process head-process">Process</div>
  <div class="abs col-head col-deliver head-deliver">Deliverables</div>

  <!-- Roles -->
  <div class="abs panel col-roles" style="top:137px;width:289px;height:248px">
    <div class="abs" style="left:16px;top:8px">
      <p class="group-title">RSQ Team</p>
      <ul class="small" style="margin-top:4px"><li>Transaction Mgr</li><li>Portfolio Advisor</li><li>Broker</li></ul>
      <p class="group-title" style="margin-top:6px">External Team</p>
      <ul class="small" style="margin-top:4px"><li>Architect</li><li>Attorney</li><li>General Contractor</li><li>IT Consultant</li></ul>
    </div>
    <div class="abs" style="left:159px;top:8px">
      <p class="group-title">Client Team</p>
      <ul class="small" style="margin-top:4px"><li>Business Unit Mgr</li><li>Corporate RE Mgr</li><li>Risk Mgr</li><li>Regional Mgr</li><li>Local Operator</li><li>CEO/CFO</li><li>VP of Finance</li><li>Administrator</li></ul>
    </div>
    <ul class="abs small" style="left:16px;top:140px;width:262px">
      <li>Evaluate requirement in light of client’s strategic plan; develop strategic plan, if appropriate.</li>
      <li>Develop project management strategy, budget, and schedules.</li>
      <li>Review critical action date report monthly.</li>
      <li>Establish KPIs.</li>
      <li>Distribute orientation binder.</li>
      <li>Review existing RSQ/Client customized Playbooks for use and applicability.</li>
    </ul>
  </div>
  <div class="abs panel col-roles" style="top:393px;width:289px;height:22px;font-size:9.3px;line-height:22px;padding-left:17px">Portfolio Advisor, Transaction Manager and/or Broker</div>
  <div class="abs panel col-roles" style="top:421px;width:289px;height:95px;padding:10px 16px 0">
    <p class="group-title">RSQ Team, Client Team, External Team</p>
    <ul class="small" style="margin-top:5px">
      <li>Develop market research comps to determine fair value,market availability, and cost.</li>
      <li>Tour market with client and create shortlist of viable buildings.</li>
      <li>Develop tour list and report to client.</li>
    </ul>
  </div>

  <!-- Process -->
  <p class="abs stage" style="left:343px;top:137px">Planning</p>
  <div class="abs step step--blue col-process" style="top:158px;height:228px">
    <span class="num" style="font-size:20px">1.</span>
    <ul class="label step-list" style="padding-left:1px">
      <li>Conduct Strategic Planning Define</li>
      <li>Client Requirements</li>
      <li>Create Budget &amp; Schedule</li>
    </ul>
    <svg width="16" height="14" viewBox="0 0 16 14" aria-hidden="true"><path d="M0 0h16L8 14z" fill="#fff"/></svg>
  </div>
  <p class="abs stage stage--teal" style="left:343px;top:393px">Evaluation</p>
  <div class="abs step step--teal col-process" style="top:414px;height:36px">
    <span class="num">2.</span><span class="label">Develop Negotiation Strategy</span>
    <svg width="16" height="14" viewBox="0 0 16 14" aria-hidden="true"><path d="M0 0h16L8 14z" fill="#fff"/></svg>
  </div>
  <div class="abs step step--teal col-process" style="top:456px;height:35px">
    <span class="num">3.</span><span class="label">Conduct Market Research and Analysis</span>
    <svg width="16" height="14" viewBox="0 0 16 14" aria-hidden="true"><path d="M0 0h16L8 14z" fill="#fff"/></svg>
  </div>
  <p class="abs end col-process" style="top:500px">END</p>

  <!-- Deliverables -->
  <div class="abs panel col-deliver" style="top:137px;width:289px;height:248px;padding:9px 0 0 17px">
    <ul class="deliv">
      <li>1.1 Pre-Engagement Documents
        <ul class="sub" style="margin-left:-17px">
          <li>Authorization Letter</li><li>Contact List</li><li>Contracts</li><li>RFQ Guidance</li><li>Service Level Agreement (2)</li><li>Commission Agreement</li><li>Standard Reporting Templates</li>
        </ul>
      </li>
      <li style="margin-top:9px">1.2 Client Needs Analysis (2)</li>
      <li style="margin-top:10px">Pre-Project Questionnaire</li>
      <li style="margin-top:10px">1.3 Strategic Plan (no deliverable)</li>
      <li style="margin-top:10px">1.4 Schedule and Budget</li>
    </ul>
  </div>
  <div class="abs panel col-deliver" style="top:393px;width:289px;height:123px;padding:20px 0 0 17px">
    <ul class="deliv">
      <li>3.1 Market Survey Template</li>
      <li style="margin-top:5px">3.2 Financial Analysis</li>
      <li style="margin-top:5px">3.3 Own vs. Lease Analysis</li>
      <li style="margin-top:5px">3.4 Building Tour Spreadsheet</li>
      <li style="margin-top:5px">3.5 Building Tour Checklist</li>
    </ul>
  </div>
</section>

<section class="sheet sheet--two">
  <p class="abs figure-label">FIGURE 5</p>
  <h1 class="abs title"><span>Space Acquisition:</span> Purchase &amp; Process Deliverables</h1>
  <div class="abs col-head col-roles head-roles">Roles &amp; Responsibilities</div>
  <div class="abs col-head col-process head-process">Process</div>
  <div class="abs col-head col-deliver head-deliver">Deliverables</div>

  <!-- Roles -->
  <div class="abs panel col-roles" style="top:137px;width:289px;height:46px;padding:8px 16px 0">
    <p class="people-title">Portfolio Advisor, Transaction Manager and/or Broker</p>
    <ul class="small" style="margin-top:8px"><li>Orchestrate competition.</li></ul>
  </div>
  <div class="abs panel col-roles" style="top:190px;width:289px;height:22px;font-size:9.3px;line-height:22px;padding-left:17px">Portfolio Advisor, Transaction Manager and/or Broker</div>
  <div class="abs panel col-roles" style="top:219px;width:289px;height:77px;padding:11px 16px 0">
    <p class="people-title">Portfolio Advisor, Transaction Manager and/or Broker, Tax Specialist, Lender Rep, Client Legal, Client Risk, Third Party Vendors</p>
    <ul class="small tiny" style="margin-top:6px"><li>Due diligence may include environmental, structural, A&amp;E, title, clarity, appraisal, financial appraisal, tax implications, etc.</li></ul>
  </div>
  <div class="abs panel col-roles" style="top:302px;width:289px;height:102px;padding:9px 16px 0">
    <p class="people-title">Portfolio Advisor, Transaction Manager and/or Broker, Project Manager, Relocation Manager, Lease Administrator</p>
    <ul class="small tiny" style="margin-top:6px">
      <li>Transaction manager brings in other service line experts (project management, lease administration), if appropriate.</li>
      <li>If RSQ is performing project mgmt, see PM Playbook.</li>
      <li>If RSQ is not performing project mgmt, coordinate with client representative or landlord.</li>
    </ul>
  </div>
  <div class="abs panel panel--dark col-roles" style="top:411px;width:289px;height:105px;padding:10px 16px 0">
    <p class="people-title" style="line-height:12px">Portfolio Advisor, Transaction Manager<br>and/or Broker</p>
    <ul class="small tiny" style="margin-top:9px">
      <li>Benchmark performance and KPIs.</li>
      <li>Submit client satisfaction forms.</li>
      <li>Complete close-out summaries and corresponding critical date reports.</li>
      <li>Create client case study, if transaction size meets criteria.</li>
    </ul>
  </div>

  <!-- Process -->
  <p class="abs stage" style="left:343px;top:137px">Execution</p>
  <div class="abs step step--blue col-process" style="top:155px;height:29px">
    <span class="num">4.</span><span class="label">Negotiate with Short List</span>
    <svg width="16" height="14" viewBox="0 0 16 14" aria-hidden="true"><path d="M0 0h16L8 14z" fill="#fff"/></svg>
  </div>
  <div class="abs step step--blue col-process" style="top:189px;height:49px">
    <span class="num">5.</span><span class="label">Negotiate/Execute LOI and Purchase &amp; Sale Agreement</span>
    <svg width="16" height="14" viewBox="0 0 16 14" aria-hidden="true"><path d="M0 0h16L8 14z" fill="#fff"/></svg>
  </div>
  <div class="abs step step--blue col-process" style="top:244px;height:52px">
    <span class="num">6.</span><span class="label">Conduct Due Diligence</span>
    <svg width="16" height="14" viewBox="0 0 16 14" aria-hidden="true"><path d="M0 0h16L8 14z" fill="#fff"/></svg>
  </div>
  <div class="abs step step--blue col-process" style="top:302px;height:102px">
    <span class="num">7.</span><span class="label">Develop Move/Project Management Documentation &amp; Transition to Project Manager, if Applicable</span>
    <svg width="16" height="14" viewBox="0 0 16 14" aria-hidden="true"><path d="M0 0h16L8 14z" fill="#fff"/></svg>
  </div>
  <p class="abs stage stage--teal" style="left:343px;top:410px">Performance</p>
  <div class="abs step step--teal col-process" style="top:429px;height:48px">
    <span class="num">8.</span><span class="label">Measure/Demonstrate Performance</span>
    <svg width="16" height="14" viewBox="0 0 16 14" aria-hidden="true"><path d="M0 0h16L8 14z" fill="#fff"/></svg>
  </div>
  <p class="abs end col-process" style="top:495px">END</p>

  <!-- Deliverables -->
  <div class="abs panel col-deliver" style="top:189px;width:289px;height:49px;padding:10px 0 0 17px">
    <ul class="deliv deliv--tight"><li>5.1 Letter of Intent</li><li>5.2 Purchase and Sale Agreement</li></ul>
  </div>
  <div class="abs panel col-deliver" style="top:244px;width:289px;height:52px;padding:10px 0 0 17px">
    <ul class="deliv deliv--tight"><li>6.1 Closing Checklist</li><li>6.2 Due Diligence Checklist</li></ul>
  </div>
  <div class="abs note-green col-deliver" style="top:302px;width:289px;height:101px">See Project Management and Facilities Management Playbooks</div>
  <div class="abs panel col-deliver" style="top:427px;width:289px;height:89px;padding:14px 0 0 17px">
    <ul class="deliv deliv--tight"><li>8.1 KPI Documentation</li><li>8.2 Client Survey</li><li>8.3 Close-Out Package</li><li>8.4 Value-Added Matrix and Scorecard</li></ul>
  </div>
</section>

</body>
</html>
```